real-estate postcard

I am a real-estate broker and want to send a postcard to expired listings saying something like"Now is the Time to think about a New Beginning with a nice looking house with a sold sign in front

Target Market(s)

people who had their homes on the market and their listing expired

Industry/Entity Type

House

Requirements
Must have
• a nice looking upscale home with a sold sign in front of it; also must have my name and contact information
Marnie Tolvath
Brightfern Realty - Ashmere Office
14 W Parlow Street
Ashmere, IL 60588
312-555-0173
Nice to have
• a saying like " Now is the time to think about new beginnings" maybe with a calendar showing it is already November

```html
<!DOCTYPE html>
<html lang="en">
<head>
<meta charset="utf-8">
<title>New Beginnings Postcard</title>
<link rel="stylesheet" href="https://fonts.googleapis.com/css2?family=Arimo:wght@400;700&family=Cinzel:wght@400;600&display=swap">
<style>
  :root {
    --olive: #a9a044;
    --olive-dark: rgba(104, 98, 40, 0.9);
    --white: #ffffff;
    --ink: #1d1d1d;
    --stage: #5b5b5b;
    --rule: #3a3a3a;
  }
  * { box-sizing: border-box; margin: 0; padding: 0; }
  html, body { width: 1200px; height: 900px; overflow: hidden; }
  body {
    background: var(--stage);
    font-family: "Arimo", Arial, sans-serif;
    position: relative;
  }
  .postcard {
    position: absolute;
    top: 255px;
    width: 570px;
    height: 390px;
    overflow: hidden;
    background: var(--white);
    box-shadow: 0 8px 24px rgba(0,0,0,0.35);
  }
  .postcard--front { left: 20px; }
  .postcard--back { left: 610px; }

  /* Front */
  .hero-photo {
    position: absolute; inset: 0;
    background: linear-gradient(160deg, #8aa36a 0%, #c9b9a0 35%, #7e8f4f 60%, #4f6b2c 100%);
  }
  .headline-panel {
    position: absolute; top: 0; right: 0;
    width: 220px; height: 230px;
  }
  .headline-panel__strip {
    position: absolute; top: 0; right: 0; width: 70px; height: 38px; background: var(--white);
  }
  .headline-panel__box {
    position: absolute; top: 38px; left: 0; right: 0; bottom: 0;
    background: var(--olive-dark);
    color: var(--white);
    font-family: "Cinzel", serif;
    text-align: center;
    padding: 14px 10px;
    line-height: 1.15;
  }
  .headline-panel__small { font-size: 15px; letter-spacing: 1px; }
  .headline-panel__big { font-size: 22px; font-weight: 600; margin-top: 6px; letter-spacing: 1px; }
  .headline-panel__rule { width: 120px; height: 1px; background: var(--white); margin: 6px auto 0; }
  .couple-photo {
    position: absolute; top: 230px; left: 340px;
    width: 150px; height: 95px;
    background: linear-gradient(180deg, #7aa3c9 0%, #d9c8a8 55%, #6f9a3f 100%);
    border: 2px solid var(--white);
  }
  .tagline {
    position: absolute; left: 22px; top: 248px;
    color: var(--white); font-weight: 700; font-size: 18px; line-height: 22px;
    white-space: nowrap;
    text-shadow: 0 1px 3px rgba(0,0,0,0.5);
  }
  .contact-box {
    position: absolute; left: 0; top: 280px;
    width: 340px; height: 82px;
    background: var(--white);
    padding: 9px 22px;
    color: var(--ink);
    line-height: 1.3;
  }
  .contact-box__name { font-weight: 700; font-size: 17px; }
  .contact-box__line { font-size: 16px; }
  .front-band {
    position: absolute; left: 0; right: 0; bottom: 0; height: 28px; background: var(--olive);
  }

  /* Back */
  .photo-pair { position: absolute; top: 22px; left: 22px; display: flex; gap: 8px; }
  .photo-pair__item { width: 128px; height: 100px; }
  .photo-pair__item--house { background: linear-gradient(180deg, #2f7fd6 0%, #9cc3e8 50%, #6f9a3f 100%); }
  .photo-pair__item--keys { background: linear-gradient(180deg, #9cc6ee 0%, #d8d2c4 55%, #8a8f7a 100%); }
  .quote {
    position: absolute; top: 136px; left: 22px; width: 290px;
    color: var(--olive); font-weight: 700; font-size: 16px; line-height: 1.25;
  }
  .services {
    position: absolute; top: 196px; left: 22px; width: 270px;
    list-style: none; font-size: 12px; font-weight: 700; color: var(--ink); line-height: 1.5;
    white-space: nowrap;
  }
  .services li::before { content: "• "; }
  .stamp-box {
    position: absolute; top: 20px; right: 20px; width: 58px; height: 68px;
    border: 1px solid var(--rule);
  }
  .address-lines { position: absolute; top: 120px; left: 340px; right: 20px; }
  .address-lines span { display: block; height: 1px; background: var(--rule); margin-bottom: 32px; }
  .agent-box {
    position: absolute; right: 20px; bottom: 20px;
    width: 250px; height: 128px;
    background: var(--olive);
    color: var(--white);
    padding: 14px 12px;
    font-weight: 700; font-size: 12.5px; line-height: 1.6;
    white-space: nowrap;
  }
</style>
</head>
<body>
  <section class="postcard postcard--front">
    <div class="hero-photo" role="img" aria-label="Upscale two-storey home with green lawn, trees and a sold sign in front"></div>
    <div class="headline-panel">
      <div class="headline-panel__strip"></div>
      <div class="headline-panel__box">
        <div class="headline-panel__small">Now is<br>the time<br>to think<br>about</div>
        <div class="headline-panel__rule"></div>
        <div class="headline-panel__big">New<br>Beginnings</div>
      </div>
    </div>
    <div class="couple-photo" role="img" aria-label="Happy couple standing in front of their new home"></div>
    <p class="tagline">We help you find your dream home</p>
    <div class="contact-box">
      <p class="contact-box__name">Marnie Tolvath</p>
      <p class="contact-box__line">Call: 312-555-0173</p>
      <p class="contact-box__line">marnietolvath@fernmail.com</p>
    </div>
    <div class="front-band"></div>
  </section>

  <section class="postcard postcard--back">
    <div class="photo-pair">
      <div class="photo-pair__item photo-pair__item--house" role="img" aria-label="Suburban house under a blue sky"></div>
      <div class="photo-pair__item photo-pair__item--keys" role="img" aria-label="Hand passing house keys in front of a sold sign"></div>
    </div>
    <p class="quote">“Committed to assisting ou with all of yourreal estate needs!”</p>
    <ul class="services">
      <li>Residential, Commercial &amp; Land</li>
      <li>Finding you the right home</li>
      <li>Helping you sell your current home</li>
      <li>Finding investment property</li>
      <li>Assisting with relocation or designing to sell</li>
      <li>Providing information for market analysis</li>
    </ul>
    <div class="stamp-box"></div>
    <div class="address-lines"><span></span><span></span><span></span></div>
    <div class="agent-box">
      <p>Marnie Tolvath</p>
      <p>Brightfern Realty - Ashmere Office</p>
      <p>14 W Parlow Street</p>
      <p>Ashmere, IL 60588</p>
      <p>312-555-0173</p>
    </div>
  </section>
</body>
</html>
```